Designer and consultant for professionals/businesses and manufacturers in the kitchen and bath in...

I have 30 years of design experience, and 19 of those years within the marketing team of a national cabinet manufacturer. This role gave me the opportunity to consult and design for kitchen/bath businesses, from boutique to multi-store national scale. My services include layout and spatial planning, individual display design, and product design for cabinet manufacturers. From showrooms, to trade shows to integrated design collections. I would like to see designs that convey professionalism, as well as an appeal to the creative designer mind!

Target Market(s)

Kitchen and bath dealers, as well as mid-scale multi-store home centers. Cabinet manufacturers, Trade Show agencies.

Industry/Entity Type

Kitchen

Contact Information for Business Card

Serving Kitchen and Bath Businesses

Logo Text

MT (initials for business name)

Font styles to use
Serif
Sans Serif
Decorative

Colors
e34197

Requirements
Must have
• Marlowe Tavish Design and Consulting, Inc. (business name)
• marlowe@mtvantra.com (email)
• 917-555-0148 (phone)
• mtvantra.com (website)
Nice to have
• Inclusions of geometric shapes; particularly a 30/15 degree triangle and circle(s)
• 2 colors
Should not have
• Not too artsy!

```html
<!DOCTYPE html>
<html lang="en">
<head>
<meta charset="utf-8">
<title>Marlowe Tavish Design and Consulting — Business Card</title>
<link rel="stylesheet" href="https://fonts.googleapis.com/css2?family=Roboto+Slab:wght@500&family=Lato:wght@400;700&display=swap">
<style>
  :root {
    --stage: #e4e4e4;
    --paper: #fcf6f5;
    --brown: #5e3a3b;
    --rose: #b95d5b;
    --ink: #3d3535;
    --rule: #8a8080;
  }
  * { box-sizing: border-box; margin: 0; padding: 0; }
  html, body { width: 1200px; height: 782px; overflow: hidden; background: var(--stage); }
  .canvas { position: relative; width: 1200px; height: 782px; }

  .card {
    position: absolute;
    top: 242px;
    width: 520px;
    height: 298px;
    overflow: hidden;
    box-shadow: 0 6px 18px rgba(0,0,0,0.18);
  }
  .card--front { left: 60px; background: var(--paper); }
  .card--back { left: 620px; background: var(--brown); }

  /* front: brand block */
  .brand { position: absolute; left: 30px; top: 34px; width: 210px; text-align: center; }
  .brand-mark {
    width: 116px; height: 116px; margin: 0 auto 10px;
    border-radius: 50%;
    border: 4px solid var(--rose);
    background: var(--brown);
    display: flex; align-items: center; justify-content: center;
    font-family: "Roboto Slab", Georgia, serif; font-weight: 500;
    font-size: 40px; color: var(--paper); letter-spacing: 2px;
  }
  .brand-name {
    font-family: "Roboto Slab", Georgia, serif; font-weight: 500;
    font-size: 23px; color: var(--brown); line-height: 1; white-space: nowrap;
  }
  .brand-tagline {
    margin-top: 4px;
    font-family: "Lato", Arial, sans-serif; font-size: 8.5px;
    letter-spacing: 2px; color: var(--rule); text-transform: uppercase; white-space: nowrap;
  }

  .divider { position: absolute; left: 272px; top: 122px; width: 1px; height: 112px; background: var(--rule); }

  .contact { position: absolute; left: 290px; top: 136px; list-style: none; }
  .contact li {
    display: flex; align-items: center; gap: 9px;
    font-family: "Lato", Arial, sans-serif; font-size: 19px; color: var(--ink);
    line-height: 30px;
  }
  .contact svg { width: 16px; height: 16px; flex: none; }

  .base-bands { position: absolute; left: 0; bottom: 0; width: 520px; height: 36px; }

  /* back */
  .back-field { position: absolute; inset: 0; background: var(--brown); }
  .back-mark {
    position: absolute; left: 328px; top: 148px;
    width: 56px; height: 56px; border-radius: 50%;
    background: var(--paper); border: 2px solid var(--paper);
    display: flex; align-items: center; justify-content: center;
    font-family: "Roboto Slab", Georgia, serif; font-weight: 500;
    font-size: 20px; color: var(--brown);
  }
</style>
</head>
<body>
<main class="canvas">

  <section class="card card--front" aria-label="Business card front">
    <div class="brand">
      <div class="brand-mark">MT</div>
      <p class="brand-name">Marlowe Tavish</p>
      <p class="brand-tagline">Design and Consulting, Inc.</p>
    </div>

    <div class="divider"></div>

    <ul class="contact">
      <li>
        <svg viewBox="0 0 16 16" aria-hidden="true"><path fill="#5e3a3b" d="M3 2h3l1 3-2 1.5a9 9 0 0 0 4.5 4.5L11 9l3 1v3a1 1 0 0 1-1 1C7 14 2 9 2 3a1 1 0 0 1 1-1z"/></svg>
        917-555-0148
      </li>
      <li>
        <svg viewBox="0 0 16 16" aria-hidden="true"><rect x="1" y="3" width="14" height="10" fill="#5e3a3b"/><path d="M1.5 3.5 8 9l6.5-5.5" fill="none" stroke="#fcf6f5" stroke-width="1.2"/></svg>
        marlowe@mtvantra.com
      </li>
      <li>
        <svg viewBox="0 0 16 16" aria-hidden="true"><circle cx="8" cy="8" r="7" fill="#5e3a3b"/><path d="M1 8h14M8 1c-3 3-3 11 0 14M8 1c3 3 3 11 0 14" fill="none" stroke="#fcf6f5" stroke-width="0.9"/></svg>
        www.mtvantra.com
      </li>
    </ul>

    <svg class="base-bands" viewBox="0 0 520 36" aria-hidden="true">
      <rect x="0" y="20" width="300" height="16" fill="var(--rose)"/>
      <polygon points="292,36 308,10 520,10 520,36" fill="var(--brown)"/>
    </svg>
  </section>

  <section class="card card--back" aria-label="Business card back">
    <div class="back-field" role="img" aria-label="Repeating pattern of faint circular initial marks in a slightly lighter brown"></div>
    <div class="back-mark">MT</div>
  </section>

</main>
</body>
</html>
```